Web Design Project

Hi, we need a new and professional design for our company "partnertradingcircuit". The website should communicate business but with a friendly and professional touch.

You can use the following categories for the menu;

Home - customer groups - products - voucher system- contact

Give it your best,

Regards,
Anselm

Industry/Entity Type

Business

```html
<!DOCTYPE html>
<html lang="en">
<head>
<meta charset="utf-8">
<title>PartnerTradingCircuit</title>
<link rel="stylesheet" href="https://fonts.googleapis.com/css2?family=Arimo:wght@400;700&family=Questrial&display=swap">
<style>
  :root{
    --blue:#1aa3dc;
    --orange:#f79b1c;
    --ink:#111;
    --grey-bg:#e8e8e8;
    --black:#000;
    --white:#fff;
  }
  *{box-sizing:border-box;margin:0;padding:0}
  html,body{width:994px;height:1200px;overflow:hidden}
  body{position:relative;background:var(--grey-bg);font-family:"Arimo",Arial,sans-serif;color:var(--ink)}
  .abs{position:absolute}

  .site-header{left:0;top:0;width:994px;height:90px;background:linear-gradient(#fbfbfb,#f1f1f1);border-bottom:1px solid #ddd}
  .brand{left:130px;top:26px;display:flex;align-items:center;gap:10px}
  .brand-dot{width:34px;height:34px;border-radius:50%;background:var(--blue)}
  .brand-name{font-family:"Questrial",sans-serif;font-size:24px;color:var(--blue)}
  .main-nav{right:50px;top:24px;display:flex}
  .main-nav a{display:block;padding:12px 9px;font-size:11.5px;font-weight:700;color:var(--ink);text-decoration:none;border-left:1px solid #e4e4e4}
  .main-nav a:first-child{border-left:0;color:var(--blue);font-weight:400}

  .sub-band{left:0;top:91px;width:994px;height:35px;background:#e9e9e9}
  .hero{left:0;top:126px;width:994px;height:386px;background:linear-gradient(100deg,#6b5140 0%,#9c8a76 35%,#c9b39a 60%,#8a6a52 100%)}
  .hero-arrow{top:292px;width:55px;height:55px;border-radius:50%;background:rgba(255,255,255,.45)}
  .hero-arrow svg{position:absolute;left:18px;top:15px}
  .hero-dots{left:466px;top:476px;display:flex;gap:7px}
  .hero-dots span{width:17px;height:17px;border-radius:50%;background:#e6e6e6;border:2px solid #fff}
  .hero-dots span.on{background:#2aa1a8}

  .h-blue{font-family:"Questrial",sans-serif;color:var(--blue);font-weight:400}
  .welcome-title{left:127px;top:552px;font-size:38px}
  .welcome-text{left:128px;top:607px;width:384px;font-size:11.3px;line-height:15px;text-align:justify}
  .team-photo{left:521px;top:609px;width:112px;height:88px;border:3px solid #fff;box-shadow:0 1px 3px rgba(0,0,0,.35);background:linear-gradient(#c7ccd1,#8d959c)}
  .what-title{left:662px;top:603px;font-size:25px}
  .what-text{left:662px;top:641px;width:190px;font-size:11.5px;line-height:19.6px}

  .services{left:0;top:741px;width:994px;height:330px;background:var(--orange)}
  .h-white{font-family:"Questrial",sans-serif;color:var(--white);font-weight:400;font-size:25px}
  .services-title{left:127px;top:749px}
  .news-title{left:662px;top:749px}
  .svc-list{list-style:none;font-size:11.5px;line-height:19.6px;color:var(--ink)}
  .svc-list li{position:relative;padding-left:11px;margin-bottom:7.5px}
  .svc-list li::before{content:"";position:absolute;left:0;top:8px;width:4px;height:4px;border-radius:50%;background:var(--ink)}
  .svc-list li.plain::before{display:none}
  .svc-left{left:128px;top:790px;width:230px}
  .svc-right{left:380px;top:790px;width:245px}
  .more-link{font-size:11px;color:var(--white)}
  .more-link a{color:var(--white)}
  .news-date{left:662px;top:792px;font-size:11.5px;color:var(--white)}
  .news-text{left:662px;top:817px;width:210px;font-size:11.5px;line-height:19.6px}
  .news-link{left:662px;top:943px;width:200px;font-size:11.5px;line-height:19.6px;color:var(--white)}

  .site-footer{left:0;top:1071px;width:994px;height:129px;background:var(--black)}
  .footer-brand{left:73px;top:1110px;font-family:"Questrial",sans-serif;font-size:20px;color:var(--white)}
  .footer-divider{left:300px;top:1102px;width:1px;height:63px;background:#aaa}
  .copyright{left:317px;top:1113px;font-size:9.5px;color:var(--white)}
  .contact-line{left:317px;top:1138px;font-size:11.5px;color:var(--white)}
  .contact-line a{color:var(--orange)}
  .socials{left:662px;top:1110px;display:flex;gap:7px}
  .socials span{width:20px;height:20px;border-radius:3px}
  .legal{left:662px;top:1142px;font-size:11.5px;color:var(--white)}
</style>
</head>
<body>
  <header class="site-header abs">
    <div class="brand abs"><span class="brand-dot"></span><span class="brand-name">PartnerTradingCircuit</span></div>
    <nav class="main-nav abs">
      <a href="#">HOME</a><a href="#">CUSTOMER GROUPS</a><a href="#">PRODUCTS</a><a href="#">VOUCHER SYSTEM</a><a href="#">CONTACT</a>
    </nav>
  </header>
  <div class="sub-band abs"></div>

  <section class="hero abs" role="img" aria-label="Woman using a laptop in a shopping mall café"></section>
  <div class="hero-arrow abs" style="left:18px"><svg width="20" height="26"><path d="M16 2 L4 13 L16 24" fill="none" stroke="#fff" stroke-width="5"/></svg></div>
  <div class="hero-arrow abs" style="left:920px"><svg width="20" height="26"><path d="M4 2 L16 13 L4 24" fill="none" stroke="#fff" stroke-width="5"/></svg></div>
  <div class="hero-dots abs"><span class="on"></span><span></span><span></span></div>

  <h1 class="welcome-title h-blue abs">Welcome!</h1>
  <p class="welcome-text abs">IPraesent ac massa nec dui faucibus ornare at ac ipsum. Curabitur tempor hendrerit ante, eget ultricies nisl viverra ac. Fusce turpis leo, vestibulum mattis porttitor sed, adipiscing in tellus. Curabitur magna urna, lobortis ut commodo ut, sollicitudin sed sapien. Maecenas vitae mi id libero vulputate egestas vitae fringilla quam. Sed ut perspiciatis unde omnis iste natus error sit voluptatem accusantium doloremque laudantium, totam rem aperiam, eaque ipsa quae ab illo inventore veritatis et quasi architecto.</p>
  <div class="team-photo abs" role="img" aria-label="Business team standing in an office"></div>
  <h2 class="what-title h-blue abs">What We Do</h2>
  <p class="what-text abs">Duis autem vel eum iriure dolor in hendrerit tum zzril delenit augue duis dolore te feugait nulla facilisi. Lorem quat vel illum augue duis dolore.</p>

  <section class="services abs"></section>
  <h2 class="services-title h-white abs">Here you can find all services in one place:</h2>
  <ul class="svc-list svc-left abs">
    <li>Broadband Internet PCs with modern LCD Flat-screens, Printers, Scanners, Webcam</li>
    <li>CD-RW/DVD-burner, Multi-card-reader, USB-Connectors</li>
    <li>Laptop/Notebook stations with LAN and/or wireless access (10mbps speed)</li>
    <li>Rentable Laptop/Notebook cabins. (Daily rent, locked and secured overnight)</li>
    <li class="plain">Stabilized UPS with world-power outlets, 220V &amp; 110V.</li>
  </ul>
  <ul class="svc-list svc-right abs">
    <li>Outdoor wireless connection available 24/7 (100m radius)</li>
    <li>Digital Photo Printer - connect your memory card, flash card, picture card, camera card, media stick or mobile phone and print the picture direct at our photo-lab-station (PrintDesk).<br>Of course you can also "unload" your camers and burn CD...</li>
  </ul>
  <p class="more-link abs" style="left:391px;top:1001px">+ <a href="#">All Services</a></p>

  <h2 class="news-title h-white abs">Latest News</h2>
  <p class="news-date abs">01 February, 2013</p>
  <p class="news-text abs">Duis autem vel eum iriure dolor in hen-drerit tum zzril delenit augue duis dolore te feugait nulla facilisi. Lorem ipsum dolor sit amet, consectetuer in vulputate velit esse molestie consequat vel illum augue duis dolore.</p>
  <p class="news-link abs"><a href="#" style="color:var(--white)">Feugiat nulla facilisis at vero eros et accumsan et iusto...</a></p>
  <p class="more-link abs" style="left:662px;top:1001px">+ <a href="#">All News</a></p>

  <footer class="site-footer abs"></footer>
  <div class="footer-brand abs">PartnerTradingCircuit</div>
  <div class="footer-divider abs"></div>
  <p class="copyright abs">Copyright © 2013 PartnerTradingCircuit. All rights reserved.</p>
  <p class="contact-line abs">Phone: +1 800 555 0142 &nbsp; Email: <a href="#">info@partnertradingcircuit.com</a></p>
  <div class="socials abs">
    <span style="background:#3b5a9a"></span><span style="background:#33aadd"></span><span style="background:#d9d9d9"></span><span style="background:#d8372b"></span>
  </div>
  <p class="legal abs">© 2013 &nbsp;I&nbsp;&nbsp; Privacy Policy</p>
</body>
</html>
```